Vel-Trax.ch is looking for business card letterhead and envelope C5 with WOW effect

We need a strong business card for our company Vel-Trax.ch, logo is available. You want a black or dark background on which the logo Stark r% 26 # 252; appears. Letterhead and envelope in C5 format should be in a similar design, but does not have to be We need a strong business card for our company Vel-Trax.ch, logo is available. A black or dark background is desired, on which the logo Stark comes across. The letterhead and the envelope in C5 format should have a similar design.

Target Market(s)

Private customers as well as entrepreneurs

Contact Information for Business Card

E-mail: info@vel-trax.ch
Web.www.Vel-Trax.ch
Tel: +41 ( 0 ) 79 684 3027
Adresse:
Lindenhaldeweg 14
8756 Brenzikon

Hier kann man Icons verwenden für Email,Tel und Adressse

Font styles to use
Other font styles liked:
• Dubai,bold

Colors

Designer to choose colors to be used in the design.

Requirements
Must have
• WOW effect
Nice to have
• R% 26 # 252; back business card with our service listings. - VEHICLE LABELING - SHOP WINDOW LABELING - STICKERS AND MUCH MORE ... in red color

```html
<!DOCTYPE html>
<html lang="de">
<head>
<meta charset="utf-8">
<title>Vel-Trax.ch – Visitenkarte</title>
<link rel="stylesheet" href="https://fonts.googleapis.com/css2?family=Open+Sans:wght@700&display=swap">
<style>
  :root {
    --stage: #9a9a9a;
    --card-base: #1d2337;
    --card-deep: #151a29;
    --glow: #2f5fc4;
    --glow-soft: #26407e;
    --accent: #fdc21e;
    --ink: #1b2033;
    --white: #ffffff;
  }
  * { margin: 0; padding: 0; box-sizing: border-box; }
  html, body { width: 1200px; height: 1200px; overflow: hidden; }
  body {
    background: var(--stage);
    font-family: "Open Sans", Arial, sans-serif;
    position: relative;
  }
  .card {
    position: absolute;
    top: 250px;
    width: 400px;
    height: 698px;
    border-radius: 0 52px 0 52px;
    overflow: hidden;
    background: var(--card-deep);
  }
  .card--front { left: 185px; }
  .card--back  { left: 615px; }
  .card__backdrop {
    position: absolute; inset: 0;
    background:
      radial-gradient(circle at 55% 45%, var(--glow) 0%, var(--glow-soft) 22%, transparent 55%),
      radial-gradient(circle at 30% 15%, rgba(60,110,210,.45) 0%, transparent 35%),
      radial-gradient(circle at 70% 85%, rgba(60,110,210,.35) 0%, transparent 40%),
      linear-gradient(180deg, var(--card-base), var(--card-deep));
  }
  .brand {
    position: absolute;
    left: 48px;
    display: flex;
    align-items: center;
    gap: 58px;
    color: var(--white);
    font-size: 28px;
    font-weight: 700;
    letter-spacing: 1px;
    white-space: nowrap;
  }
  .brand__mark {
    width: 42px; height: 42px;
    background: var(--accent);
    flex: none;
  }
  .card--front .brand { top: 326px; }
  .card--back  .brand { top: 131px; }
  .contact-list {
    position: absolute;
    left: 68px;
    top: 422px;
    list-style: none;
  }
  .contact-item {
    width: 266px;
    height: 30px;
    margin-bottom: 9.5px;
    background: var(--accent);
    clip-path: polygon(10px 0, 100% 0, calc(100% - 10px) 50%, 100% 100%, 10px 100%, 0 50%);
    display: flex;
    align-items: center;
    padding-left: 22px;
    gap: 12px;
    color: var(--ink);
    font-size: 18px;
    font-weight: 700;
    white-space: nowrap;
  }
  .contact-item--plain { padding-left: 56px; }
  .contact-item svg { width: 22px; height: 22px; flex: none; }
</style>
</head>
<body>
  <section class="card card--front">
    <div class="card__backdrop" role="img" aria-label="Dunkelblauer Hintergrund mit leuchtendem Netzwerk aus Punkten und Linien"></div>
    <div class="brand"><span class="brand__mark"></span><span class="brand__name">VEL-TRAX.CH</span></div>
  </section>

  <section class="card card--back">
    <div class="card__backdrop" role="img" aria-label="Dunkelblauer Hintergrund mit leuchtendem Netzwerk aus Punkten und Linien"></div>
    <div class="brand"><span class="brand__mark"></span><span class="brand__name">VEL-TRAX.CH</span></div>
    <ul class="contact-list">
      <li class="contact-item">
        <svg viewBox="0 0 22 22" fill="none" stroke="#1b2033" stroke-width="1.4"><circle cx="11" cy="11" r="10"/><circle cx="11" cy="11" r="6"/><ellipse cx="11" cy="11" rx="2.6" ry="6"/><line x1="5" y1="11" x2="17" y2="11"/></svg>
        <span>www.Vel-Trax.ch</span>
      </li>
      <li class="contact-item">
        <svg viewBox="0 0 22 22" fill="none" stroke="#1b2033" stroke-width="1.4"><circle cx="11" cy="11" r="10"/><rect x="5.5" y="7.5" width="11" height="7.5"/><polyline points="5.5,7.5 11,12 16.5,7.5"/></svg>
        <span>info@vel-trax.ch</span>
      </li>
      <li class="contact-item">
        <svg viewBox="0 0 22 22"><circle cx="11" cy="11" r="10" fill="none" stroke="#1b2033" stroke-width="1.4"/><path d="M5 9c0-2 2-3 6-3s6 1 6 3l-2 1-1-1.5h-6L7 10z" fill="#1b2033"/><rect x="6.5" y="11" width="9" height="5" rx="1" fill="#1b2033"/></svg>
        <span>+41 ( 0 ) 79 684 3027</span>
      </li>
      <li class="contact-item">
        <svg viewBox="0 0 22 22" fill="none" stroke="#1b2033" stroke-width="1.4"><circle cx="11" cy="11" r="10"/><path d="M11 17s-4-4-4-7a4 4 0 0 1 8 0c0 3-4 7-4 7z"/><circle cx="11" cy="10" r="1.4"/></svg>
        <span>Lindenhaldeweg 14</span>
      </li>
      <li class="contact-item contact-item--plain">
        <span>8756 Brenzikon</span>
      </li>
    </ul>
  </section>
</body>
</html>
```